Executive Business Card for Healthcare Company [Need Today]

I need a business card design for a healthcare company. The only branding the company has thus far is a logo. The cards will be utilized by company executives. The design I envision will be vibrant and appealing but with a corporate feel. They shouldn't be too casual or playful. I would like to complete this project TODAY if possible.

Target Market(s)

Healthcare vendors, other executives in healthcare and pharmaceuticals

Industry/Entity Type

Pharmaceutical

Contact Information for Business Card

See attachment

Font styles to use
Serif
Sans Serif

Colors

Designer to choose colors to be used in the design.

```html
<!DOCTYPE html>
<html lang="en">
<head>
<meta charset="utf-8">
<title>Lunveri Therapeutics – Executive Business Card</title>
<link rel="stylesheet" href="https://fonts.googleapis.com/css2?family=Lato:wght@300;400;700&display=swap">
<style>
  :root {
    --backdrop: #ece6d4;
    --card: #ffffff;
    --teal: #33bec7;
    --ink: #1f1f1f;
    --ink-soft: #3a3a3a;
    --divider: #b8b8b8;
    --shadow: rgba(80, 70, 40, 0.22);
  }
  * { margin: 0; padding: 0; box-sizing: border-box; }
  html, body { width: 1200px; height: 1200px; overflow: hidden; }
  body {
    background: var(--backdrop);
    font-family: "Lato", sans-serif;
    position: relative;
  }
  .card {
    position: absolute;
    left: 165px;
    width: 870px;
    height: 497px;
    background: var(--card);
    box-shadow: 0 14px 34px var(--shadow);
    overflow: hidden;
  }
  .card--front { top: 70px; }
  .card--back { top: 633px; }

  /* Front */
  .brand-band {
    position: absolute;
    left: 0; top: 0;
    width: 380px; height: 100%;
    background: var(--teal);
    overflow: hidden;
  }
  .brand-band svg { position: absolute; left: 0; top: 0; }
  .contact {
    position: absolute;
    left: 445px; top: 62px;
    color: var(--ink);
  }
  .contact__name { font-weight: 700; font-size: 25px; letter-spacing: 0.2px; }
  .contact__title { font-weight: 400; font-size: 16px; color: var(--ink-soft); margin-top: 2px; }
  .contact__group { margin-top: 52px; }
  .contact__group + .contact__group { margin-top: 26px; }
  .contact__line {
    display: flex; align-items: center; gap: 10px;
    font-size: 21px; font-weight: 400; line-height: 30px;
  }
  .contact__icon { width: 22px; height: 22px; flex: none; }
  .contact__address {
    margin-top: 24px;
    font-size: 22px; font-weight: 700; line-height: 30px;
  }

  /* Back */
  .lockup {
    position: absolute;
    left: 0; right: 0; top: 50%;
    transform: translateY(-50%);
    display: flex; align-items: center; justify-content: center; gap: 34px;
  }
  .lockup__circle {
    width: 180px; height: 180px;
    border: 5px solid var(--teal);
    border-radius: 50%;
    flex: none;
  }
  .lockup__divider { width: 2px; height: 150px; background: var(--divider); }
  .lockup__name {
    font-weight: 400; font-size: 56px; color: var(--teal);
    line-height: 1.05; letter-spacing: 0.5px;
  }
</style>
</head>
<body>

  <section class="card card--front">
    <div class="brand-band">
      <svg width="380" height="497" viewBox="0 0 380 497" aria-hidden="true">
        <circle cx="125" cy="250" r="212" fill="none" stroke="#ffffff" stroke-width="7"/>
      </svg>
    </div>

    <div class="contact">
      <div class="contact__name">Marcus Hale</div>
      <div class="contact__title">Senior Director of Marketing</div>

      <div class="contact__group">
        <div class="contact__line">
          <svg class="contact__icon" viewBox="0 0 22 22" aria-hidden="true"><circle cx="11" cy="11" r="11" fill="var(--teal)"/><rect x="7.5" y="4.5" width="7" height="13" rx="1.5" fill="#fff"/><rect x="8.8" y="6.3" width="4.4" height="8" fill="var(--teal)"/></svg>
          <span>555-210-4837</span>
        </div>
        <div class="contact__line">
          <svg class="contact__icon" viewBox="0 0 22 22" aria-hidden="true"><circle cx="11" cy="11" r="11" fill="var(--teal)"/><path d="M5 9.5c0-2 2.7-3.2 6-3.2s6 1.2 6 3.2v1h-3v-1.6h-6v1.6H5z" fill="#fff"/><rect x="6.5" y="11.5" width="9" height="5" rx="1" fill="#fff"/></svg>
          <span>555-362-9104</span>
        </div>
      </div>

      <div class="contact__group">
        <div class="contact__line">
          <svg class="contact__icon" viewBox="0 0 22 22" aria-hidden="true"><circle cx="11" cy="11" r="11" fill="var(--teal)"/><rect x="5" y="7" width="12" height="8.5" rx="1" fill="#fff"/><path d="M5.5 7.6 11 11.8l5.5-4.2" fill="none" stroke="var(--teal)" stroke-width="1.3"/></svg>
          <span>mhale@lunverirx.com</span>
        </div>
        <div class="contact__line">
          <svg class="contact__icon" viewBox="0 0 22 22" aria-hidden="true"><circle cx="11" cy="11" r="11" fill="var(--teal)"/><circle cx="11" cy="11" r="6" fill="none" stroke="#fff" stroke-width="1.4"/><ellipse cx="11" cy="11" rx="2.6" ry="6" fill="none" stroke="#fff" stroke-width="1.2"/><path d="M5 11h12" stroke="#fff" stroke-width="1.2"/></svg>
          <span>www.lunverirx.com</span>
        </div>
      </div>

      <div class="contact__address">118 N Harbor Avenue<br>Dayton, OH 45402</div>
    </div>
  </section>

  <section class="card card--back">
    <div class="lockup">
      <div class="lockup__circle"></div>
      <div class="lockup__divider"></div>
      <div class="lockup__name">Lunveri<br>Therapeutics</div>
    </div>
  </section>

</body>
</html>
```